Design for a very long wall that will be wall printed. The name of the facility is "Bright Gallery"

The space I am working on has a 30' x 8' wall. It is a wall that is located in a under construction Design Showroom where contractors of all trades can have an office and put out their banners and different items for customers to come and see. so there could be roofers, construction, cabinet installers and designers, gutters and other trades can rent an office in the space and bring their customers and sit down and talk about what they need. I want the design for the wall to have a bold punch and it will be printed on the wall with a high definition wall printer. The walls are arctic white right now and I can send the color codes for the color the wall is currently. The wall printer has the capability to do white as well. I am including some pics of the space and an example wall print.

Target Market(s)

Contractors and Customers of Contractors

Industry/Entity Type

all trades. Photos are to demonstrate the capabilities of the printer that will be used

Requirements
Must have
• Perhaps have a person or persons int he design, a human element and perhaps some abstract elements as well
Nice to have
• Perhaps some architecture or perhaps an interior cabinet or fixtures. Glass doors and or walls. Perhaps incorporate the name "Bright Gallery"

```html
<!DOCTYPE html>
<html lang="en">
<head>
<meta charset="UTF-8">
<title>Bright Gallery – Wall Mural</title>
<link href="https://fonts.googleapis.com/css2?family=Montserrat:wght@600&display=swap" rel="stylesheet">
<style>
  :root {
    --stage: #333333;
    --paper: #ffffff;
    --orange: #f79a00;
    --navy: #111a33;
    --grey: #888888;
    --photo-light: #e9e3dc;
    --photo-dark: #c98a2e;
  }
  html, body {
    margin: 0;
    padding: 0;
    width: 1200px;
    height: 1200px;
    overflow: hidden;
    background: var(--stage);
  }
  .mural {
    display: block;
    width: 1200px;
    height: 1200px;
  }
  .mural__paper { fill: var(--paper); }
  .mural__accent { fill: var(--orange); }
  .mural__dot--navy { fill: var(--navy); }
  .mural__dot--orange { fill: var(--orange); }
  .mural__cross { stroke: var(--navy); stroke-width: 6; stroke-linecap: butt; }
  .mural__cross--muted { stroke: var(--grey); }
  .mural__title {
    font-family: "Montserrat", sans-serif;
    font-weight: 600;
    font-size: 126px;
  }
  .mural__title--fill { fill: var(--orange); }
  .mural__title--outline { fill: none; stroke: var(--grey); stroke-width: 2.5; }
</style>
</head>
<body>
<svg class="mural" viewBox="0 0 1500 1500" xmlns="http://www.w3.org/2000/svg">
  <defs>
    <linearGradient id="photo-tone" x1="0" y1="0" x2="0" y2="1">
      <stop offset="0" stop-color="var(--photo-light)"/>
      <stop offset="0.7" stop-color="#e2d8cc"/>
      <stop offset="1" stop-color="var(--photo-dark)"/>
    </linearGradient>
  </defs>

  <!-- banner base -->
  <rect class="mural__paper" x="85" y="578" width="1329" height="354"/>

  <!-- left frame block -->
  <rect class="mural__accent" x="85" y="578" width="222" height="354"/>
  <rect class="mural__paper" x="134" y="627" width="173" height="257"/>
  <rect class="mural__accent" x="85" y="884" width="695" height="48"/>

  <!-- top-right band -->
  <rect class="mural__accent" x="926" y="578" width="488" height="66"/>

  <!-- tradesperson photo area -->
  <rect x="118" y="590" width="252" height="342" rx="4" fill="url(#photo-tone)"
        role="img" aria-label="Photo of a smiling tradeswoman in a white t-shirt, work gloves and tool belt, making a call-me gesture"/>

  <!-- crosses -->
  <g class="mural__crosses">
    <path class="mural__cross mural__cross--muted" d="M352 592 L378 618 M378 592 L352 618"/>
    <path class="mural__cross" d="M422 592 L448 618 M448 592 L422 618"/>
    <path class="mural__cross" d="M492 592 L518 618 M518 592 L492 618"/>
    <path class="mural__cross" d="M562 592 L588 618 M588 592 L562 618"/>
  </g>

  <!-- navy dot rows -->
  <g class="mural__dot--navy">
    <rect x="884" y="624" width="12" height="12"/>
    <rect x="940" y="624" width="12" height="12"/>
    <rect x="996" y="624" width="12" height="12"/>
    <rect x="1052" y="624" width="12" height="12"/>
    <rect x="1108" y="624" width="12" height="12"/>
    <rect x="1164" y="624" width="12" height="12"/>
    <rect x="940" y="654" width="12" height="12"/>
    <rect x="996" y="654" width="12" height="12"/>
    <rect x="1052" y="654" width="12" height="12"/>
    <rect x="1108" y="654" width="12" height="12"/>
    <rect x="1164" y="654" width="12" height="12"/>
    <rect x="1220" y="654" width="12" height="12"/>
  </g>

  <!-- orange dot staircase -->
  <g class="mural__dot--orange">
    <rect x="1363" y="720" width="14" height="14"/>
    <rect x="1363" y="756" width="14" height="14"/>
    <rect x="1363" y="792" width="14" height="14"/>
    <rect x="1363" y="829" width="14" height="14"/>
    <rect x="1363" y="865" width="14" height="14"/>
    <rect x="1363" y="902" width="14" height="14"/>
    <rect x="1302" y="792" width="14" height="14"/>
    <rect x="1302" y="829" width="14" height="14"/>
    <rect x="1302" y="865" width="14" height="14"/>
    <rect x="1302" y="902" width="14" height="14"/>
    <rect x="1242" y="792" width="14" height="14"/>
    <rect x="1242" y="829" width="14" height="14"/>
    <rect x="1242" y="865" width="14" height="14"/>
    <rect x="1242" y="902" width="14" height="14"/>
    <rect x="1182" y="829" width="14" height="14"/>
    <rect x="1182" y="865" width="14" height="14"/>
    <rect x="1182" y="902" width="14" height="14"/>
    <rect x="1122" y="865" width="14" height="14"/>
    <rect x="1122" y="902" width="14" height="14"/>
    <rect x="1062" y="902" width="14" height="14"/>
  </g>

  <!-- facility name -->
  <text class="mural__title mural__title--fill" x="362" y="796" textLength="984" lengthAdjust="spacingAndGlyphs">Bright Gallery</text>
  <text class="mural__title mural__title--outline" x="366" y="800" textLength="984" lengthAdjust="spacingAndGlyphs" aria-hidden="true">Bright Gallery</text>
</svg>
</body>
</html>
```